Webdesign

We are value investment firm in Denver, Colorado. We are a small but a very unique firm. We are looking for a minimalistic and clean design. We are competing against competitors that usually larger than we are, but we need to have a design that is better than theirs. Our clients put a tremendous trust in us when they let us manage their life savings. This website has to communicate trust but without traditional cliches (dollar bills, glasses, Harbor Ledger Gazette).
We had a coder/designer create our current website a few weeks ago http://brightkestrel.example/tolvan , we are not thrilled about the design. We are attaching our company's presentation, we'd like the design to be closer to the colors of that presentation.
We are looking for both design and coding (wordpress).
Updates
we will pay additional $200 for wordpress implementation
A few points of clarifications about design:
- don't use pictures of strangers
- we are a Denver/Colorado firm, if you use pictures use Denver/Colorado pictures
- full width website is probably what we are looking
- maybe parallax type of design
This theme http://quillframe.example/WP/Nimbra/ is how we see the new design
Industry/Entity Type
Investment

```html
<!DOCTYPE html>
<html lang="en">
<head>
<meta charset="utf-8">
<title>Tolvan — Value Investment</title>
<link href="https://fonts.googleapis.com/css2?family=Open+Sans:wght@300;400;600&display=swap" rel="stylesheet">
<style>
:root{
  --navy:#1f2f6e;
  --ink:#3a3a3a;
  --muted:#8a8a8a;
  --soft:#f4f4f4;
  --line:#e2e2e2;
  --footer:#262626;
  --field:#3a3a3a;
  --field-text:#8d8d8d;
  --accent:#3856a8;
  --white:#ffffff;
}
*{margin:0;padding:0;box-sizing:border-box}
html,body{width:875px;height:1200px;overflow:hidden}
body{font-family:"Open Sans",Arial,sans-serif;color:var(--ink);background:var(--white);position:relative}
.abs{position:absolute}

/* header */
.site-header{position:absolute;left:0;top:0;width:875px;height:80px;background:var(--white)}
.brand{left:174px;top:24px;font-weight:600;font-size:25px;line-height:30px;letter-spacing:1px;color:var(--navy);display:flex;align-items:center;gap:7px}
.brand-square{width:12px;height:12px;background:var(--navy)}
.nav-item{top:37px;font-size:6.5px;line-height:9px;letter-spacing:.2px;text-transform:uppercase;color:var(--muted);white-space:nowrap}
.nav-item.active{color:var(--navy)}
.nav-item.active::after{content:"";position:absolute;left:0;right:0;top:17px;height:2px;background:var(--navy)}
.nav-divider{left:717px;top:36px;width:1px;height:11px;background:var(--line)}
.nav-search{left:726px;top:37px}

/* intro */
.intro{left:0;top:80px;width:875px;height:58px;background:var(--soft);display:flex;align-items:center;justify-content:center;text-align:center;font-size:9px;line-height:13px;color:var(--muted)}

/* hero */
.hero{left:0;top:138px;width:875px;height:264px;background:linear-gradient(120deg,#2c3a5a 0%,#6d7f9c 30%,#dfe6ef 55%,#f3f5f8 75%,#c9d4e2 100%)}
.hero-title{left:176px;top:250px;font-size:24px;font-weight:300;color:var(--white)}
.hero-text{left:176px;top:286px;width:220px;font-size:10.5px;line-height:13px;color:var(--white)}

/* strengths */
.section-title{left:174px;top:437px;font-size:23px;font-weight:300;color:#4a4a4a}
.laptop-shot{left:174px;top:488px;width:240px;height:130px;background:linear-gradient(180deg,#1c1c1c 0%,#3e5a8c 45%,#cfd8e4 80%,#b9bcc1 100%);border-radius:4px}
.feature{width:150px}
.feature h3{font-size:11px;font-weight:400;color:#555;display:flex;align-items:center;gap:8px;margin-bottom:8px}
.feature p{font-size:7.5px;line-height:12px;color:var(--muted)}

/* quote */
.quote-band{left:0;top:665px;width:875px;height:194px;background:linear-gradient(180deg,#2c4690 0%,#3a56a0 55%,#4a63a8 100%)}
.quote{left:0;top:745px;width:875px;text-align:center;color:var(--white);font-size:14.5px;line-height:22px}

/* footer */
.site-footer{left:0;top:859px;width:875px;height:341px;background:var(--footer)}
.footer-title{left:174px;top:887px;font-size:17px;font-weight:300;color:#e6e6e6}
.footer-lead{left:174px;top:914px;width:170px;font-size:6px;line-height:8px;color:#9a9a9a}
.form-label{left:174px;top:946px;font-size:8px;color:#d8d8d8}
.field{left:174px;width:200px;height:24px;background:var(--field);color:var(--field-text);font-size:6.5px;padding:8px 10px}
.field.tall{height:77px}
.send-btn{left:284px;top:1128px;height:24px;display:flex}
.send-btn .label{width:99px;background:#3d3d3d;color:#d0d0d0;font-size:6.5px;font-weight:600;letter-spacing:.4px;display:flex;align-items:center;justify-content:center}
.send-btn .tick{width:24px;background:var(--accent);display:flex;align-items:center;justify-content:center}
.footer-links{left:174px;top:1164px;font-size:6px;color:#bdbdbd}
.copyright{left:174px;top:1177px;font-size:6px;color:#bdbdbd}
.footer-brand{left:488px;top:904px;font-size:21px;line-height:26px;font-weight:600;letter-spacing:1px;color:#8a8a8a;display:flex;align-items:center;gap:7px}
.footer-brand .brand-square{width:10px;height:10px;background:#8a8a8a}
.map{left:486px;top:970px;width:247px;height:87px;background:linear-gradient(135deg,#d6d6d6,#eeeeee 50%,#cfcfcf);border-radius:3px}
.address-title{left:488px;top:1073px;font-size:8px;color:#d8d8d8}
.address{left:488px;top:1090px;font-size:6px;line-height:9px;color:#a5a5a5}
.contact-line{left:488px;font-size:6px;color:#a5a5a5;display:flex;align-items:center;gap:6px}
</style>
</head>
<body>

<header class="site-header">
  <div class="abs brand"><span class="brand-square"></span>TOLVAN</div>
  <nav>
    <span class="abs nav-item active" style="left:434px">Home</span>
    <span class="abs nav-item" style="left:473px">About Us</span>
    <span class="abs nav-item" style="left:520px">Invest Diffently</span>
    <span class="abs nav-item" style="left:589px">Content</span>
    <span class="abs nav-item" style="left:635px">Career</span>
    <span class="abs nav-item" style="left:671px">Contact Us</span>
  </nav>
  <div class="abs nav-divider"></div>
  <svg class="abs nav-search" width="8" height="8" viewBox="0 0 10 10"><circle cx="4" cy="4" r="3" fill="none" stroke="#9a9a9a" stroke-width="1"/><line x1="6.3" y1="6.3" x2="9.3" y2="9.3" stroke="#9a9a9a" stroke-width="1"/></svg>
</header>

<div class="abs intro"><p>A disciplined, process-driven, value investment firm that provides a private portfolio management service tailored to individual<br>and institutional clients tired of in-the-box, cookie-cutter, buy-and-hope investment products.</p></div>

<section>
  <div class="abs hero" role="img" aria-label="Photo of hands with a pen reviewing printed financial charts on a desk"></div>
  <h1 class="abs hero-title">We Are Different</h1>
  <p class="abs hero-text">Our Active Value investment approach is crafted specifically for today's treacherous sideways market.</p>
</section>

<section>
  <h2 class="abs section-title">Strength of Our Business</h2>
  <div class="abs laptop-shot" role="img" aria-label="Laptop showing the website homepage"></div>

  <div class="abs feature" style="left:434px;top:487px">
    <h3><svg width="11" height="12" viewBox="0 0 11 12"><circle cx="5.5" cy="4.5" r="4" fill="#9a9a9a"/><rect x="3.8" y="8.5" width="3.4" height="2.5" fill="#9a9a9a"/></svg>Idea</h3>
    <p>Sed tincidunt, erat in malesuada aliquam, est erat faucibus purus, eget viverra nulla sem vitae.</p>
  </div>
  <div class="abs feature" style="left:597px;top:487px">
    <h3><svg width="12" height="12" viewBox="0 0 12 12"><path d="M1 11l1-3 6-6 2 2-6 6z" fill="#9a9a9a"/></svg>Sketch &amp; Design</h3>
    <p>Sed tincidunt, erat in malesuada aliquam, est erat faucibus purus, eget viverra nulla sem vitae.</p>
  </div>
  <div class="abs feature" style="left:434px;top:560px">
    <h3><svg width="12" height="12" viewBox="0 0 12 12"><circle cx="7.5" cy="4.5" r="3.3" fill="none" stroke="#9a9a9a" stroke-width="1.6"/><line x1="5" y1="7" x2="1.5" y2="10.5" stroke="#9a9a9a" stroke-width="2"/></svg>Develop</h3>
    <p>Sed tincidunt, erat in malesuada aliquam, est erat faucibus purus, eget viverra nulla sem vitae.</p>
  </div>
  <div class="abs feature" style="left:597px;top:560px">
    <h3><svg width="12" height="12" viewBox="0 0 12 12"><circle cx="6" cy="6" r="5" fill="none" stroke="#9a9a9a" stroke-width="1.4"/><circle cx="6" cy="6" r="2.2" fill="none" stroke="#9a9a9a" stroke-width="1.2"/></svg>Support</h3>
    <p>Sed tincidunt, erat in malesuada aliquam, est erat faucibus purus, eget viverra nulla sem vitae.</p>
  </div>
</section>

<section>
  <div class="abs quote-band" role="img" aria-label="Blue-tinted Denver city skyline"></div>
  <blockquote class="abs quote">Design is not just what it looks like and feels like. Design is how it works.<br>Elden Marsh</blockquote>
</section>

<footer class="abs site-footer"></footer>
<h2 class="abs footer-title">Get to know us completely just</h2>
<p class="abs footer-lead">Lorem Ipsum is simply dummy text of the printing and typesetting industry</p>
<p class="abs form-label">Contact Form</p>
<div class="abs field" style="top:969px">Name</div>
<div class="abs field" style="top:1005px">Email</div>
<div class="abs field tall" style="top:1043px">Message</div>
<div class="abs send-btn">
  <span class="label">SEND MESSAGE</span>
  <span class="tick"><svg width="9" height="8" viewBox="0 0 9 8"><path d="M1 4l2.5 2.5L8 1" fill="none" stroke="#fff" stroke-width="1.5"/></svg></span>
</div>
<p class="abs footer-links">Home &nbsp;|&nbsp; About Us &nbsp;|&nbsp; Invest Diffently &nbsp;|&nbsp; Content &nbsp;|&nbsp; Career &nbsp;|&nbsp; Contact Us</p>
<p class="abs copyright">Copyright © 2014 Tolvan &nbsp;|&nbsp; PRIVACY POLICY</p>

<div class="abs footer-brand"><span class="brand-square"></span>TOLVAN</div>
<div class="abs map" role="img" aria-label="Street map with office location marker"></div>
<p class="abs address-title">Address</p>
<p class="abs address">#42, Sample Road, Town<br>Springfield, ST 54321</p>
<div class="abs contact-line" style="top:1120px"><svg width="7" height="7" viewBox="0 0 8 8"><path d="M1 1h2l1 2-1 1c.6 1.2 1.2 1.8 2 2l1-1 2 1v2C4 8 0 4 1 1z" fill="#8a8a8a"/></svg>+12 55501 234567</div>
<div class="abs contact-line" style="top:1132px"><svg width="7" height="6" viewBox="0 0 8 6"><rect width="8" height="6" fill="#8a8a8a"/><path d="M0 0l4 3 4-3" fill="none" stroke="#262626" stroke-width=".8"/></svg>support@tolvan.example</div>
<div class="abs contact-line" style="top:1144px"><svg width="7" height="7" viewBox="0 0 8 8"><circle cx="4" cy="4" r="3.5" fill="#8a8a8a"/><path d="M.5 4h7M4 .5c-2 2-2 5 0 7M4 .5c2 2 2 5 0 7" fill="none" stroke="#262626" stroke-width=".6"/></svg>www.tolvan.example</div>

</body>
</html>
```